Flyer Design Dental Office Grand Opening offer

Dental office.

Grand opening flyer. Offer Exam + cleaning + xrays.
special: free teeth whitening ($200 value)

Target Market(s)

Middle class people around Huntington Beach.

Industry/Entity Type

Dental Clinic

Colors
cfeae6
86cfc6
fac994
fee18a
e667a6

Requirements
Must have
• Do not change my existing logo
Nice to have
• Have some appealing picture/design to catch the eye, but not too flashy
Should not have
• No cartoon kind of design

```html
<!DOCTYPE html>
<html lang="en">
<head>
<meta charset="utf-8">
<title>Harbor Smile – Grand Opening Flyer</title>
<link href="https://fonts.googleapis.com/css2?family=Anton&family=Lato:wght@400;700;900&display=swap" rel="stylesheet">
<style>
  :root {
    --orange: #ec6a2c;
    --orange-dark: #d9561a;
    --teal: #1aa3bf;
    --teal-dark: #118aa6;
    --ink: #1e1e1e;
    --paper: #ffffff;
    --ray: #f1f1f1;
    --skin-light: #f3d3bd;
    --skin-mid: #dcae8f;
    --hair: #b98f5e;
  }
  * { margin: 0; padding: 0; box-sizing: border-box; }
  html, body { width: 777px; height: 1200px; overflow: hidden; background: var(--paper); }
  .flyer {
    position: relative;
    width: 777px;
    height: 1200px;
    overflow: hidden;
    background:
      radial-gradient(ellipse at 50% 80%, var(--paper) 0%, var(--paper) 30%, var(--ray) 100%);
    font-family: "Lato", sans-serif;
    color: var(--ink);
  }
  .hero-art { position: absolute; left: 0; top: 0; width: 777px; height: 720px; }

  .brand {
    position: absolute;
    right: 40px;
    top: 112px;
    text-align: right;
  }
  .brand-name {
    display: flex;
    align-items: center;
    gap: 12px;
    font-family: "Lato", sans-serif;
    font-weight: 900;
    font-size: 40px;
    color: var(--teal);
    line-height: 1;
  }
  .brand-mark { width: 22px; height: 22px; border-radius: 50%; background: var(--orange); }
  .brand-doctor { margin-top: 8px; font-size: 13px; color: var(--ink); }

  .headline {
    position: absolute;
    right: 34px;
    top: 258px;
    width: 330px;
    text-align: center;
    font-family: "Anton", sans-serif;
    line-height: 1.08;
    text-shadow: 1px 2px 2px rgba(0,0,0,0.18);
  }
  .headline-grand { display: block; font-size: 100px; color: var(--orange); }
  .headline-opening { display: block; font-size: 86px; color: var(--teal); }

  .offer {
    position: absolute;
    left: 0;
    top: 715px;
    width: 777px;
    text-align: center;
  }
  .offer-price {
    font-family: "Anton", sans-serif;
    font-size: 108px;
    line-height: 1;
    letter-spacing: -1px;
    text-shadow: 1px 2px 2px rgba(0,0,0,0.2);
  }
  .offer-price .exam { color: var(--orange); }
  .offer-price .price { color: var(--teal); }
  .offer-detail { font-size: 33px; margin-top: 8px; }
  .offer-bonus {
    font-family: "Anton", sans-serif;
    font-size: 46px;
    line-height: 1;
    margin-top: 18px;
  }
  .offer-bonus .service { color: var(--teal); }
  .offer-bonus .free { color: var(--orange); }
  .offer-note { font-size: 28px; margin-top: 4px; }

  .insurance-band {
    position: absolute;
    left: 0;
    top: 1000px;
    width: 777px;
    height: 98px;
    background: var(--orange);
    color: var(--paper);
    font-weight: 700;
    font-size: 41px;
    display: flex;
    align-items: center;
    justify-content: center;
  }

  .contact {
    position: absolute;
    left: 0;
    top: 1128px;
    width: 777px;
    display: flex;
    justify-content: center;
    align-items: center;
    gap: 34px;
  }
  .contact-item { display: flex; align-items: center; gap: 10px; }
  .contact-phone { font-weight: 900; font-size: 26px; }
  .contact-address { font-size: 20px; }
  .contact-icon { width: 26px; height: 26px; }
</style>
</head>
<body>
<main class="flyer">

  <svg class="hero-art" viewBox="0 0 777 720">
    <defs>
      <linearGradient id="photoTone" x1="0" y1="0" x2="1" y2="1">
        <stop offset="0" stop-color="var(--hair)"/>
        <stop offset="0.35" stop-color="var(--skin-mid)"/>
        <stop offset="0.7" stop-color="var(--skin-light)"/>
        <stop offset="1" stop-color="#f6ece6"/>
      </linearGradient>
      <linearGradient id="photoFade" x1="0" y1="0" x2="1" y2="0">
        <stop offset="0.7" stop-color="#fff" stop-opacity="0"/>
        <stop offset="1" stop-color="#fff" stop-opacity="1"/>
      </linearGradient>
    </defs>
    <g role="img" aria-label="Photo of a smiling young woman with shoulder-length blond hair">
      <path d="M0,0 H430 V635 C330,690 150,700 0,560 Z" fill="url(#photoTone)"/>
      <path d="M0,0 H430 V635 C330,690 150,700 0,560 Z" fill="url(#photoFade)"/>
    </g>
    <path class="wave-teal" d="M0,565 C110,700 280,705 430,640 S690,560 777,505" fill="none" stroke="var(--teal)" stroke-width="9"/>
    <path class="wave-orange" d="M390,650 C540,610 690,575 777,470 L777,490 C690,590 540,625 390,660 Z" fill="var(--orange)"/>
  </svg>

  <header class="brand">
    <div class="brand-name"><span class="brand-mark"></span>Harbor Smile</div>
    <div class="brand-doctor">Lena Park, DDS</div>
  </header>

  <h1 class="headline">
    <span class="headline-grand">GRAND</span>
    <span class="headline-opening">OPENING</span>
  </h1>

  <section class="offer">
    <div class="offer-price"><span class="exam">EXAM</span> <span class="price">$50</span></div>
    <p class="offer-detail">with Xrays &amp; cleaning (regular)</p>
    <p class="offer-bonus"><span class="service">TEETH WHITENING</span> <span class="free">FREE</span></p>
    <p class="offer-note">(after completion of dental treatment)</p>
  </section>

  <div class="insurance-band">PPO, HMO, DentiCal Welcomed</div>

  <footer class="contact">
    <div class="contact-item">
      <svg class="contact-icon" viewBox="0 0 24 24" aria-hidden="true">
        <circle cx="12" cy="12" r="10.5" fill="none" stroke="var(--teal)" stroke-width="1.8"/>
        <path d="M8.2 6.5c.5-.4 1.2-.3 1.5.2l1.1 1.8c.3.5.2 1.1-.2 1.4l-.8.6c.6 1.4 1.6 2.4 3 3l.6-.8c.3-.4.9-.5 1.4-.2l1.8 1.1c.5.3.6 1 .2 1.5l-.8.9c-.6.6-1.5.8-2.3.4-2.6-1.2-4.5-3.1-5.7-5.7-.4-.8-.2-1.7.4-2.3z" fill="var(--teal)"/>
      </svg>
      <span class="contact-phone">714 555 0182</span>
    </div>
    <div class="contact-item">
      <svg class="contact-icon" viewBox="0 0 24 24" aria-hidden="true">
        <path d="M12 2.5c-3.6 0-6.5 2.8-6.5 6.4 0 4.6 6.5 12.6 6.5 12.6s6.5-8 6.5-12.6c0-3.6-2.9-6.4-6.5-6.4zm0 9a2.6 2.6 0 1 1 0-5.2 2.6 2.6 0 0 1 0 5.2z" fill="var(--teal)"/>
      </svg>
      <span class="contact-address">1280 Seabright Ave., Huntington Beach, CA 92649</span>
    </div>
  </footer>

</main>
</body>
</html>
```